Stationery for London Estate Agents (Real Estate)

We are a modern and professional Estate Agency (Realtors) working with high quality properties in London.
We wish to redesign our stationary using our branding displayed on the front of our offices and require a digital version of this logo to be produced (photograph attached). Slight 'tweaking' of this branding is acceptable.
Updates
1st July 2010 Thank you all those designers who have uploaded submissions. Business Card - Details Side: Business Card - Logo Side: Outline of London Skyline Examples of the london skyline are available at http://www.pictovantix.com/searchkwy_london-skyline-silhouette Please be advised that we are looking for an outline, not a 'filled in' silhouette. Letterhead Please feel free to ask us any questions. Bertrand
I have been able to further refine our design requirements based on your submissions.
We like Pale Forks' business card submission that has not been eliminated and have the following design clarifications;
a) Please use an email icon (e.g an envelope).
b) Please make the email as equally prominent as the telephone and fax
c) We very much like VelloTrine's 'mini window icon' - please display the website URL under such a mini window icon at the bottom right of the card.
We are very happy with the colouring, fonts and proportions used by Pale Forks.
We invite designers to try adding an outline of the London Skyline to the left of the large window icon on the business card and in a suitablie position on the Letterhead (e.g at the top left of the letterhead).
We have the following design clarifiications to our Letterhead requirements;
A) We would like the main logo to be on the top right side of the letterhead.
B) We do NOT want the large window icon to be on the left of the logo or the bottom of the letterhead. We are happy having the large window icon to the right or underneath the KB brand.
C) Please use icons for tel, fax and email (e.g. envelope icon for e-mail address)
D) We like two coloured red borders, one at the top and bottom of the letterhead but are happy for variations in shape and size.
E) We currently prefer our address and contact details at the bottom of the letterhead.
F) We like VelloTrine's 'mini window icon' and would prefer this to be used to display the website URL at the bottom right of the letterhead.
G) Please be advised that the letterhead does NOT need additional space for the Company Name as per Pale Forks' submission - the KB brand is sufficient.
Target Market(s)
Owners of high quality property in London.
Industry/Entity Type
Real Estate
Requirements
Must have
- Business Cards: We would like a 'vertical' style business card with our branding on one side and our staff's details on the other;
- Our website is www.korbend.com and we are flexible where that should be on the card and letterhead.
- Stationery details are available in a file attached to this project.
Nice to have
- It would be great to have a horizontal version of the digital logo for placement on property portals (150x60)
Should not have
- Logo should not deviate significantly from the branding on our offices (shop front) - photograph attached.

```html
<!DOCTYPE html>
<html lang="en">
<head>
<meta charset="utf-8">
<title>Korbend Residential – Business Cards &amp; Banner Head</title>
<link rel="stylesheet" href="https://fonts.googleapis.com/css2?family=Arimo:wght@400;700&display=swap">
<style>
  :root {
    --brand-red: #c5303f;
    --brand-yellow: #f8cf5c;
    --ink: #111111;
    --paper: #ffffff;
    --font: "Arimo", Arial, sans-serif;
  }
  * { margin: 0; padding: 0; box-sizing: border-box; }
  html, body {
    width: 1200px; height: 899px; overflow: hidden;
    background: var(--paper); font-family: var(--font); color: var(--ink);
  }
  .sheet { position: relative; width: 1200px; height: 899px; }
  .spec-label { position: absolute; font-size: 16px; line-height: 1; white-space: nowrap; }
  .sheet-title {
    position: absolute; left: 753px; top: 138px;
    font-size: 40px; font-weight: 400; line-height: 50px;
  }
  .panel { position: absolute; background: var(--brand-red); color: var(--paper); }
  .line {
    position: absolute; left: 0; right: 0; text-align: center;
    white-space: nowrap; line-height: 1;
  }
  .bold { font-weight: 700; }
  .accent-square { position: absolute; background: var(--brand-yellow); }

  /* business card front */
  .card-front { left: 70px; top: 95px; width: 247px; height: 384px; }
  .card-front .brand-name { font-size: 27px; font-weight: 700; }
  .card-front .service { font-size: 21px; font-weight: 700; }

  /* business card back */
  .card-back { left: 354px; top: 95px; width: 246px; height: 384px; }
  .card-back .person { font-size: 18px; font-weight: 700; }
  .card-back .detail { font-size: 15px; }
  .card-back .web { font-size: 18px; font-weight: 700; }

  /* property portal banner */
  .portal-banner { left: 453px; top: 573px; width: 680px; height: 271px; }
  .portal-banner .brand-name { font-size: 62px; font-weight: 700; left: 0; right: 120px; }
  .portal-banner .web { font-size: 35px; font-weight: 700; left: 0; right: 120px; }
</style>
</head>
<body>
<main class="sheet">
  <p class="spec-label" style="left:71px; top:70px;">Bcard - front:</p>
  <p class="spec-label" style="left:236px; top:70px;">55x85mm</p>
  <p class="spec-label" style="left:356px; top:70px;">Bcard - back:</p>

  <h1 class="sheet-title">Business Cards<br>&amp; Banner Head</h1>

  <section class="panel card-front" aria-label="Business card front">
    <p class="line brand-name" style="top:38px;">KORBEND</p>
    <p class="line brand-name" style="top:72px;">RESIDENTIAL</p>
    <p class="line service" style="top:133px;">Lettings</p>
    <p class="line service" style="top:165px;">Sales</p>
    <p class="line service" style="top:197px;">Management</p>
    <p class="line service" style="top:229px;">Investments</p>
    <span class="accent-square" style="left:160px; top:300px; width:66px; height:66px;"></span>
  </section>

  <section class="panel card-back" aria-label="Business card back">
    <p class="line person" style="top:39px;">Bertrand Hale</p>
    <p class="line detail" style="top:78px;">284 Larkmoor Road</p>
    <p class="line detail" style="top:104px;">Hampstead</p>
    <p class="line detail" style="top:129px;">London</p>
    <p class="line detail" style="top:154px;">NW3 9QX</p>
    <p class="line detail" style="top:191px;">t: 020 7946 0418</p>
    <p class="line detail" style="top:217px;">f: 020 7946 0527</p>
    <p class="line detail" style="top:242px;">m: 07700 900 316</p>
    <p class="line detail" style="top:279px;">e: bertrand@korbend.com</p>
    <p class="line web" style="top:334px;">www.korbend.com</p>
  </section>

  <p class="spec-label" style="left:456px; top:546px;">PROPERTY PORTALS BANNER - 150x60:</p>

  <section class="panel portal-banner" aria-label="Property portals banner">
    <p class="line brand-name" style="top:30px;">KORBEND</p>
    <p class="line brand-name" style="top:112px;">RESIDENTIAL</p>
    <p class="line web" style="top:196px;">www.korbend.com</p>
    <span class="accent-square" style="left:570px; top:168px; width:86px; height:86px;"></span>
  </section>
</main>
</body>
</html>
```